Stationery Design Project

Require letterhead/stationery design based on new logo (see attached).

Would prefer it kept simple but strong and effective.

Target Market(s)

Clients and building developers. Residential/consumer and corporate clientele.

```html
<!DOCTYPE html>
<html lang="en">
<head>
<meta charset="utf-8">
<title>Arcvale Projects – Stationery</title>
<link href="https://fonts.googleapis.com/css2?family=Montserrat:wght@400;500;600&family=Cormorant+Garamond:wght@500&display=swap" rel="stylesheet">
<style>
  :root{
    --bg:#d8d5d3;
    --paper:#fbf8f6;
    --ink:#2c2b2c;
    --ink-soft:#6d6b6c;
    --rule:#b9b6b5;
    --brand-blue:#1c9ad6;
    --brand-dark:#2b2a2b;
    --white:#ffffff;
  }
  *{box-sizing:border-box;margin:0;padding:0}
  html,body{width:1200px;height:890px;overflow:hidden}
  body{background:var(--bg);font-family:"Montserrat",Arial,sans-serif;color:var(--ink);position:relative}

  /* Letterhead */
  .letterhead{position:absolute;left:70px;top:55px;width:550px;height:780px;background:var(--paper);box-shadow:0 6px 18px rgba(0,0,0,.12)}
  .letterhead__corner{position:absolute;right:0;top:0;width:22px;height:22px;background:#8d8b8c}
  .brand{display:flex;align-items:center;gap:10px}
  .brand__mark{width:22px;height:22px;background:var(--brand-blue)}
  .brand__name{font-weight:600;letter-spacing:.12em;text-transform:uppercase;font-size:17px;color:var(--ink-soft)}
  .letterhead .brand{position:absolute;right:44px;top:150px}
  .letterhead__date{position:absolute;right:44px;top:190px;font-size:8.5px;color:var(--ink-soft);text-align:right}
  .recipient{position:absolute;left:60px;top:110px;font-size:8.5px;line-height:1.55;color:var(--ink-soft)}
  .letter-body{position:absolute;left:60px;top:250px;width:430px;font-size:9.5px;line-height:1.7;color:var(--ink)}
  .letter-body p{margin-bottom:11px}
  .signoff{position:absolute;left:60px;top:520px;font-size:9px;line-height:1.6}
  .signoff__signature{width:90px;height:34px;margin:6px 0;background:linear-gradient(90deg,#e9e6e4,#dad7d5)}
  .signoff__name{font-weight:600}
  .signoff__role{color:var(--ink-soft)}
  .contact-block{position:absolute;left:0;bottom:0;width:220px;height:118px;background:var(--brand-blue);color:var(--white);padding:18px 20px;font-size:9px;line-height:1.6}
  .contact-block__label{font-weight:600;letter-spacing:.08em}

  /* Business cards */
  .card{position:absolute;width:350px;height:200px;box-shadow:0 6px 16px rgba(0,0,0,.15)}
  .card--back{left:720px;top:90px;background:var(--brand-dark)}
  .card--back .brand{position:absolute;left:50%;top:50%;transform:translate(-50%,-50%)}
  .card--back .brand__name{color:#9a9899}
  .card--back .card__flap{position:absolute;right:0;top:0;width:0;height:0;border-top:38px solid #3e3d3e;border-left:38px solid transparent}
  .card--front{left:720px;top:340px;background:var(--paper)}
  .card__square{position:absolute;left:0;top:0;width:26px;height:26px;background:var(--brand-blue)}
  .card__stripe{position:absolute;left:0;top:40px;bottom:0;width:6px;background:var(--brand-blue)}
  .card__name{position:absolute;left:40px;top:58px;font-family:"Cormorant Garamond",Georgia,serif;font-size:28px;color:var(--brand-blue)}
  .card__details{position:absolute;left:40px;top:100px;font-size:9px;line-height:1.75;color:var(--ink-soft)}
  .card__rule{position:absolute;right:0;bottom:0;width:350px;height:4px;background:var(--rule)}
</style>
</head>
<body>

<section class="letterhead" aria-label="Letterhead">
  <div class="letterhead__corner"></div>

  <div class="recipient">
    Mr. Daniel Reyes<br>Site Director<br>14 Harbour Lane<br>Northfield
  </div>

  <div class="brand">
    <span class="brand__mark"></span>
    <span class="brand__name">Arcvale Projects</span>
  </div>
  <div class="letterhead__date">November 27, 2016</div>

  <div class="letter-body">
    <p>Dear Mr. Reyes,</p>
    <p>Thank you for the opportunity to present our proposal for the residential development at Harbour Lane. Our team has reviewed the site plans and prepared a detailed schedule covering design, approvals and construction stages.</p>
    <p>We work closely with developers and homeowners alike, keeping every project on time and within budget. Please find the full estimate enclosed, and do not hesitate to contact our office with any questions.</p>
    <p>We look forward to building with you.</p>
  </div>

  <div class="signoff">
    Kind regards,
    <div class="signoff__signature" role="img" aria-label="Handwritten signature"></div>
    <div class="signoff__name">Your Name</div>
    <div class="signoff__role">Senior Manager</div>
  </div>

  <div class="contact-block">
    <div class="contact-block__label">ADDRESS</div>
    <div>12 Quarry Road, Eastbrook</div>
    <div class="contact-block__label">CONTACT NO.</div>
    <div>+1 234 567 89</div>
    <div>email@youremail.com</div>
    <div>www.yourwebsite.com</div>
  </div>
</section>

<section class="card card--back" aria-label="Business card back">
  <div class="card__flap"></div>
  <div class="brand">
    <span class="brand__mark"></span>
    <span class="brand__name">Arcvale Projects</span>
  </div>
</section>

<section class="card card--front" aria-label="Business card front">
  <div class="card__square"></div>
  <div class="card__stripe"></div>
  <div class="card__name">Your Name</div>
  <div class="card__details">
    +1 234 567 89<br>
    12 Quarry Road, Eastbrook<br>
    email@youremail.com<br>
    www.yourwebsite.com
  </div>
  <div class="card__rule"></div>
</section>

</body>
</html>
```